Willow Bloom Services Business Card Design

I require a business card design for my business Willow Bloom Services. The purpose of this business is to enable people to make positive change in their lives. This business offers life coaching, hypnotherapy and facilitation services. The slogan is 'Rise from the ashes and live the life you want.' Coaching services will be available internationally whilst the hypnotherapy and facilitation services will focus on delivery in south east Queensland.

The business card should be crisp, clean, professional and give the client positive feelings of achieving success.

The logo must be representative of a phoenix rising from the ashes which is a symbol of regeneration and new life. My preference is a black Phoenix on a white background similar to the Phoenix image attached to this brief. I'm happy to see other concepts you have too. The logo and business name must be scalable so it can be printed on a large outdoor sign. Therefore the following files must be provided as a minimum:
-Business card
-Logo on it's own
-Business name on it's own

The following detail must appear on either the front/back of the business card
-Logo
-Willow Bloom Services
-Rise from the ashes and live the life you want.
-Personal and business success through
-Coaching | Hypnotherapy | Facilitation
-Della Harcourt
-Founder

-Life Coach
-Clinical Hypnotherapist
-MBA (Project Management specialisation)
-Neuro Linguistic Programming Practitioner

-0418 372 906
-E: willowbloom.au@mailhaven.com
-www.willow-bloom.com.au
-Contact us now for your free 20min assessment

Please feel free to ask me as many questions as you like :) Thank you.

Hi all,  friendly reminder that the logo needs to be your own design and cannot be a Imagequarry or other purchased or free image.  

Thanks heaps
Keep the great designs coming in. You're all so talented.
Della

• Feedback from older people is that black backgrounds with lighter fonts are difficult to read so please no black backgrounds.

```html
<!DOCTYPE html>
<html lang="en">
<head>
<meta charset="utf-8">
<title>Willow Bloom Services – Business Card</title>
<link rel="stylesheet" href="https://fonts.googleapis.com/css2?family=Arimo:wght@400;700&display=swap">
<style>
  :root {
    --brand-green: #5aab84;
    --brand-green-soft: rgba(90, 171, 132, 0.55);
    --brand-green-clear: rgba(90, 171, 132, 0);
    --ink: #111111;
    --paper: #ffffff;
    --card-edge: #8a8a8a;
    --emblem-dark: #0c0c0c;
  }
  * { box-sizing: border-box; margin: 0; padding: 0; }
  html, body {
    width: 1022px;
    height: 1200px;
    overflow: hidden;
    background: var(--paper);
    font-family: "Arimo", Arial, sans-serif;
    color: var(--ink);
  }
  .sheet { position: relative; width: 1022px; height: 1200px; }

  .card {
    position: absolute;
    left: 79px;
    width: 861px;
    height: 528px;
    border: 1.5px solid var(--card-edge);
    background: var(--paper);
    overflow: hidden;
  }
  .card--front { top: 60px; }
  .card--back  { top: 634px; }

  .accent-wash {
    position: absolute;
    top: 0;
    bottom: 0;
    width: 190px;
  }
  .accent-wash--left {
    left: 0;
    background: linear-gradient(to right, var(--brand-green-soft), var(--brand-green-clear));
  }
  .accent-wash--right {
    right: 0;
    bottom: 49px;
    background: linear-gradient(to left, var(--brand-green-soft), var(--brand-green-clear));
  }

  /* Front */
  .emblem {
    position: absolute;
    left: 340px;
    top: 14px;
    width: 182px;
    height: 396px;
    background: var(--emblem-dark);
  }
  .phone {
    position: absolute;
    top: 16px;
    right: 14px;
    display: flex;
    align-items: center;
    gap: 8px;
    color: var(--brand-green);
    font-weight: 700;
    font-size: 29px;
  }
  .phone svg { width: 26px; height: 26px; fill: var(--brand-green); }
  .business-name {
    position: absolute;
    top: 418px;
    left: 0;
    right: 0;
    text-align: center;
    color: var(--brand-green);
    font-weight: 700;
    font-size: 47px;
    letter-spacing: 0.2px;
  }
  .name-rule {
    position: absolute;
    top: 476px;
    left: 154px;
    width: 543px;
    height: 2px;
    background: var(--ink);
  }
  .tagline {
    position: absolute;
    top: 484px;
    left: 0;
    right: 0;
    text-align: center;
    font-weight: 700;
    font-size: 23px;
  }

  /* Back */
  .offer {
    position: absolute;
    top: 16px;
    left: 0;
    right: 0;
    text-align: center;
    font-weight: 700;
    font-size: 25px;
  }
  .credentials {
    position: absolute;
    top: 84px;
    left: 30px;
    list-style: none;
    font-size: 24px;
    line-height: 53px;
  }
  .credentials li::before { content: "•"; margin-right: 10px; }
  .contact-band {
    position: absolute;
    left: 0;
    right: 0;
    bottom: 0;
    height: 49px;
    background: var(--brand-green);
    display: flex;
    align-items: center;
    justify-content: space-between;
    padding: 0 16px 0 14px;
    font-size: 24px;
  }
  .contact-band span { display: flex; align-items: center; gap: 8px; }
  .contact-band svg { width: 24px; height: 20px; fill: none; stroke: var(--ink); stroke-width: 1.6; }
</style>
</head>
<body>
<main class="sheet">

  <section class="card card--front" aria-label="Business card front">
    <div class="accent-wash accent-wash--left" role="img" aria-label="Green decorative corner pattern"></div>
    <div class="emblem" role="img" aria-label="Logo emblem: black panel with a white rising phoenix"></div>
    <p class="phone">
      <svg viewBox="0 0 24 24" aria-hidden="true"><path d="M3 8c0-2 2-4 9-4s9 2 9 4v2h-5V8H8v2H3zM6 11h12l3 8H3z"/></svg>
      0418 372 906
    </p>
    <h1 class="business-name">Willow Bloom Services</h1>
    <div class="name-rule"></div>
    <p class="tagline">Rise from the ashes and live the life you want.</p>
  </section>

  <section class="card card--back" aria-label="Business card back">
    <div class="accent-wash accent-wash--right" role="img" aria-label="Green decorative corner pattern"></div>
    <h2 class="offer">Contact us now for your free 20min assessment</h2>
    <ul class="credentials">
      <li>Personal and business success through</li>
      <li>Coaching | Hypnotherapy | Facilitation</li>
      <li>Della Harcourt MBA specializing in project management</li>
      <li>Founder</li>
      <li>Certified Clinical Hypnotherapist</li>
      <li>Certified Neuro Linguistic Programming Practitioner</li>
      <li>Certified Life Coach</li>
    </ul>
    <footer class="contact-band">
      <span>
        <svg viewBox="0 0 24 20" aria-hidden="true"><rect x="1" y="2" width="22" height="16"/><path d="M1 2l11 9 11-9"/></svg>
        willowbloom.au@mailhaven.com
      </span>
      <span>
        <svg viewBox="0 0 24 20" aria-hidden="true"><path d="M8 18V7a2 2 0 0 1 4 0v5l5 1v5"/></svg>
        www.willow-bloom.com.au
      </span>
    </footer>
  </section>

</main>
</body>
</html>
```